FernPath Promotions Flyer Design

I need to be able to have a flyer that shows what I do for businesses. Same logo that you designed.

Requirements
Must have
• I gave an example of what I need it to say in the attachment. Must have logo and resemble business card style.
Nice to have
• It could include pictures of what a digital sign is. We offer an KVTA, weather, and news slide on our advertising. I included sample pictures of those.

```html
<!DOCTYPE html>
<html lang="en">
<head>
<meta charset="utf-8">
<title>FernPath Promotions Flyer</title>
<link href="https://fonts.googleapis.com/css2?family=Montserrat:wght@600;700&family=Source+Sans+3:wght@400;600;700&display=swap" rel="stylesheet">
<style>
  :root {
    --page-bg: #141414;
    --green: #6fad28;
    --green-light: #8cc63f;
    --charcoal: #4a4a4a;
    --charcoal-dark: #3c3c3c;
    --text-grey: #555555;
    --heading-grey: #5a5a5a;
    --white: #ffffff;
    --sky-top: #7fbfe6;
    --sky-mid: #d6ecf7;
    --grass: #5f8f2c;
    --soil: #3a2c22;
  }
  * { margin: 0; padding: 0; box-sizing: border-box; }
  html, body {
    width: 1200px; height: 2234px; overflow: hidden;
    background: var(--page-bg);
  }
  .flyer {
    position: absolute; left: 0; top: 341px;
    width: 1200px; height: 1551px;
    background: var(--white);
    overflow: hidden;
    font-family: "Source Sans 3", Arial, sans-serif;
    color: var(--text-grey);
  }
  .hero-photo {
    position: absolute; left: 0; top: 0; width: 1200px; height: 640px;
    background:
      linear-gradient(to bottom, transparent 0%, transparent 74%, var(--grass) 80%, var(--soil) 90%, var(--soil) 100%),
      linear-gradient(to bottom, var(--sky-top) 0%, var(--sky-mid) 45%, #eef7fb 70%);
  }
  .flyer-shapes { position: absolute; left: 0; top: 0; width: 1200px; height: 1551px; }
  .brand-name {
    position: absolute; left: 62px; top: 100px;
    font-family: "Montserrat", Arial, sans-serif; font-weight: 700;
    font-size: 78px; line-height: 1; color: var(--heading-grey);
    letter-spacing: -1px;
  }
  .brand-name span { display: block; font-size: 40px; letter-spacing: 14px; margin-top: 8px; }
  .intro {
    position: absolute; left: 62px; top: 630px; width: 530px;
  }
  .intro-title {
    font-family: "Montserrat", Arial, sans-serif; font-weight: 700;
    font-size: 43px; color: var(--heading-grey); letter-spacing: -0.5px;
    margin-bottom: 26px;
  }
  .section-title {
    font-family: "Source Sans 3", Arial, sans-serif; font-weight: 700;
    color: var(--green); font-size: 26px; margin-bottom: 12px;
  }
  .section-title.small { font-size: 22px; margin-top: 54px; }
  .tick-list { list-style: none; }
  .tick-list li {
    position: relative; padding-left: 24px;
    font-size: 17px; line-height: 22.5px; text-align: justify;
    margin-bottom: 12px;
  }
  .tick-list li svg { position: absolute; left: 0; top: 5px; width: 14px; height: 14px; }
  .tick-list b { font-weight: 700; color: var(--heading-grey); }
  .process-tab {
    position: absolute; left: 604px; top: 670px; width: 300px; height: 38px;
    background: var(--charcoal); color: var(--white);
    border-radius: 0 19px 19px 0;
    font-family: "Montserrat", Arial, sans-serif; font-weight: 600;
    font-size: 25px; line-height: 38px; padding-left: 44px;
  }
  .process-steps {
    position: absolute; left: 649px; top: 738px; width: 458px;
    color: var(--white); font-size: 16.5px; line-height: 22.5px;
  }
  .step { margin-bottom: 22px; text-align: justify; }
  .step-label { font-weight: 700; font-size: 18px; display: block; }
  .step.tight { margin-bottom: 12px; }
  .call-out { font-weight: 700; }
</style>
</head>
<body>
<div class="flyer">
  <div class="hero-photo" role="img" aria-label="Photo of a young green seedling growing from a strip of grass and soil under a bright blue sky"></div>

  <svg class="flyer-shapes" viewBox="0 0 1200 1551" aria-hidden="true">
    <defs>
      <clipPath id="body-area">
        <path d="M0,615 C320,560 760,640 1200,520 L1200,1551 L0,1551 Z"/>
      </clipPath>
    </defs>
    <path d="M0,615 C320,560 760,640 1200,520 L1200,1551 L0,1551 Z" fill="#ffffff"/>
    <path class="process-panel" clip-path="url(#body-area)"
          d="M616,450 H1138 V1280 Q1138,1308 1110,1308 H644 Q616,1308 616,1280 Z" fill="#6fad28"/>
    <path d="M0,600 C320,545 760,625 1200,495" fill="none" stroke="#4a4a4a" stroke-width="26"/>
    <path d="M0,612 C320,557 760,637 1200,515" fill="none" stroke="#8cc63f" stroke-width="10"/>
    <path d="M0,1335 C300,1415 800,1400 1200,1300" fill="none" stroke="#8cc63f" stroke-width="12"/>
    <path d="M0,1385 C300,1440 800,1430 1200,1350 L1200,1551 L0,1551 Z" fill="#4a4a4a"/>
    <g class="image-slots" fill="#ffffff" stroke="#6fad28" stroke-width="5">
      <ellipse cx="208" cy="1443" rx="141" ry="72"/>
      <ellipse cx="601" cy="1443" rx="141" ry="72"/>
      <ellipse cx="992" cy="1443" rx="141" ry="72"/>
    </g>
  </svg>

  <div class="brand-name">FernPath<span>PROMOTIONS</span></div>

  <section class="intro">
    <h1 class="intro-title">FernPath Promotions</h1>
    <h2 class="section-title">What We Do</h2>
    <ul class="tick-list">
      <li><svg viewBox="0 0 14 14"><rect x="1" y="2" width="10" height="10" fill="none" stroke="#6fad28" stroke-width="1.6"/><path d="M3.5,6.5 L6,9.5 L13,1.5" fill="none" stroke="#6fad28" stroke-width="2"/></svg>We provide monthly payments to businesses for allowing us to advertise local businesses on a TV screen in your place of business.</li>
      <li><svg viewBox="0 0 14 14"><rect x="1" y="2" width="10" height="10" fill="none" stroke="#6fad28" stroke-width="1.6"/><path d="M3.5,6.5 L6,9.5 L13,1.5" fill="none" stroke="#6fad28" stroke-width="2"/></svg>We provide the TV screen if you prefer (professional installation on our dime)</li>
      <li><svg viewBox="0 0 14 14"><rect x="1" y="2" width="10" height="10" fill="none" stroke="#6fad28" stroke-width="1.6"/><path d="M3.5,6.5 L6,9.5 L13,1.5" fill="none" stroke="#6fad28" stroke-width="2"/></svg>We provide a win/win for the businesses that partner with us. Our business partners get paid to support local businesses.</li>
    </ul>
    <h2 class="section-title small">Benefits of Partnering with FernPath Promotions</h2>
    <ul class="tick-list">
      <li><svg viewBox="0 0 14 14"><rect x="1" y="2" width="10" height="10" fill="none" stroke="#6fad28" stroke-width="1.6"/><path d="M3.5,6.5 L6,9.5 L13,1.5" fill="none" stroke="#6fad28" stroke-width="2"/></svg>WE PAY YOU!</li>
      <li><svg viewBox="0 0 14 14"><rect x="1" y="2" width="10" height="10" fill="none" stroke="#6fad28" stroke-width="1.6"/><path d="M3.5,6.5 L6,9.5 L13,1.5" fill="none" stroke="#6fad28" stroke-width="2"/></svg>We advertise local businesses and business owners. We encourage them to stop by your establishment to check out their ad. This will create more foot traffic to your business.</li>
      <li><svg viewBox="0 0 14 14"><rect x="1" y="2" width="10" height="10" fill="none" stroke="#6fad28" stroke-width="1.6"/><path d="M3.5,6.5 L6,9.5 L13,1.5" fill="none" stroke="#6fad28" stroke-width="2"/></svg><b>Waiting Rooms:</b> Studies show perceived wait time can be decreased by up to 33% when there is digital signage present. This can make your clients’ 60 min wait feel like a 40 min wait.</li>
      <li><svg viewBox="0 0 14 14"><rect x="1" y="2" width="10" height="10" fill="none" stroke="#6fad28" stroke-width="1.6"/><path d="M3.5,6.5 L6,9.5 L13,1.5" fill="none" stroke="#6fad28" stroke-width="2"/></svg>Professional ticker at the bottom of the digital design can display sports updates, breaking news, and weather. Our design approach makes your business look more professional.</li>
      <li><svg viewBox="0 0 14 14"><rect x="1" y="2" width="10" height="10" fill="none" stroke="#6fad28" stroke-width="1.6"/><path d="M3.5,6.5 L6,9.5 L13,1.5" fill="none" stroke="#6fad28" stroke-width="2"/></svg>Did we mention that we pay you?!!!</li>
    </ul>
  </section>

  <div class="process-tab">Effortless Process</div>
  <section class="process-steps">
    <p class="step"><span class="step-label">DAY 1:</span>Sign on to partner with FernPath Promotions.</p>
    <p class="step"><span class="step-label">WEEK 1:</span>We install a HDMI/USB drive to the screen. Our onsite time for this is less than 10 minutes and this WILL NOT disrupt your business operations. In fact, you may not even notice we came and went. (We can use an existing screen or install a new screen at no cost to you if space permits)</p>
    <p class="step"><span class="step-label">WEEK 1-8:</span>We will be loading our local advertisers’ professional designs to the screen. (This is done remotely and does not require us to come in)</p>
    <p class="step"><span class="step-label">END OF 2ND FULL MONTH:</span>Process is complete, and you will be receiving monthly checks!</p>
    <p class="step tight">Notice your involvement is only in the first and last step. Sign-up. Get Paid.</p>
    <p class="step tight">We will pay you ______________________ each month.</p>
    <p class="step call-out">Call, text, or email for details!</p>
  </section>
</div>
</body>
</html>
```